KORBLE Development is an idea development firm. This business card is for Weekend Wicket League, a site that allows users from all over the world to play fantasy cricket against each other.
We need a business card for WWL using our logo and its associated colors. The cards are for the two founders, Tobias Whitlow and Martin Dobrescu. We would like our own cards.
We are handing our card to potential investors and sponsors of our site. It needs to be unique (like our brand.)
Updates
I wanted to thank everyone for their awesome designs!!! It was a hard choice - we narrowed it down to 7 then to three then to 1. All of you are extremely talented - THANK YOU.
Target Market(s)
Potential Investors, Partners
Industry/Entity Type
Business
Contact Information for Business Card
Korble Development : Weekend Wicket League
Tobias Whitlow
Founder
555-204-7316
tobias@korble.example
www.weekendwicketleague.example
....
Martin Dobrescu
Founder
555-871-0492
martin@korble.example
Look and feel

```html
<!DOCTYPE html>
<html lang="en">
<head>
<meta charset="utf-8">
<title>Weekend Wicket League – Business Card</title>
<link rel="stylesheet" href="https://fonts.googleapis.com/css2?family=Oswald:wght@300;400&family=Open+Sans:wght@400;600;700&family=Questrial&display=swap">
<style>
  :root {
    --stage: #e9e9ea;
    --white: #ffffff;
    --green-light: #86c440;
    --green-mid: #5fae3c;
    --green-deep: #2f8a3a;
    --green-dark: #1e6f2c;
    --ink: #1a1a1a;
  }
  * { box-sizing: border-box; margin: 0; padding: 0; }
  html, body {
    width: 1200px; height: 900px; overflow: hidden;
    background: var(--stage);
  }
  .stage {
    width: 1200px; height: 900px;
    display: flex; align-items: center; justify-content: center; gap: 40px;
  }
  .card {
    position: relative;
    width: 540px; height: 310px;
    border-radius: 22px;
    overflow: hidden;
    background: linear-gradient(180deg, var(--green-mid) 0%, var(--green-light) 45%, var(--green-deep) 100%);
    box-shadow: 0 10px 24px rgba(0,0,0,0.18);
  }
  .card-shapes { position: absolute; inset: 0; }
  .brand-mark {
    position: absolute;
    display: flex; align-items: center; gap: 8px;
    font-family: "Oswald", sans-serif; font-weight: 400;
    color: var(--green-dark);
  }
  .brand-mark .dot {
    width: 18px; height: 18px; border-radius: 50%;
    background: var(--green-dark);
  }
  .front .brand-mark { left: 42px; top: 128px; font-size: 34px; }
  .back .brand-mark { left: 36px; top: 128px; font-size: 34px; color: var(--white); }
  .back .brand-mark .dot { background: var(--white); }

  .title {
    position: absolute;
    font-family: "Oswald", sans-serif; font-weight: 300;
    color: var(--white);
    text-shadow: 0 1px 2px rgba(0,0,0,0.25);
    white-space: nowrap;
  }
  .front .title { left: 244px; top: 22px; font-size: 28px; }
  .person { position: absolute; left: 250px; top: 92px; font-family: "Open Sans", sans-serif; }
  .person-name { color: var(--green-dark); font-weight: 600; font-size: 18px; }
  .person-role { color: var(--white); font-size: 15px; margin-top: 2px; }
  .contacts {
    position: absolute; left: 240px; top: 168px;
    list-style: none;
    font-family: "Open Sans", sans-serif; font-size: 15px; color: var(--white);
  }
  .contacts li { display: flex; align-items: center; gap: 6px; height: 22px; }
  .contacts svg { width: 15px; height: 15px; flex: none; }
  .company {
    position: absolute; top: 266px;
    font-family: "Questrial", sans-serif; font-size: 15px;
    white-space: nowrap;
  }
  .company-first { left: 30px; letter-spacing: 10px; color: var(--green-deep); }
  .company-second { left: 182px; letter-spacing: 12px; color: var(--white); }

  .back .title { left: 188px; top: 110px; font-size: 38px; }
  .tagline {
    position: absolute; left: 196px; top: 170px;
    font-family: "Open Sans", sans-serif; font-weight: 700; font-size: 14px;
    color: var(--ink);
  }
</style>
</head>
<body>
<main class="stage">

  <section class="card front">
    <svg class="card-shapes" viewBox="0 0 540 310" aria-hidden="true">
      <path d="M0 0 H200 C190 110 180 215 150 310 H0 Z" fill="var(--white)"/>
      <path d="M200 0 H226 C214 110 198 215 163 310 H150 C180 215 190 110 200 0 Z" fill="var(--green-dark)"/>
      <path d="M229 0 C217 110 201 215 166 310" fill="none" stroke="var(--white)" stroke-width="4"/>
    </svg>
    <div class="brand-mark"><span class="dot"></span>WWL</div>
    <h1 class="title">Weekend Wicket League</h1>
    <div class="person">
      <p class="person-name">Tobias Whitlow</p>
      <p class="person-role">Founder</p>
    </div>
    <ul class="contacts">
      <li>
        <svg viewBox="0 0 24 24"><path fill="var(--green-dark)" d="M6.6 10.8a15 15 0 0 0 6.6 6.6l2.2-2.2a1 1 0 0 1 1-.25 11.4 11.4 0 0 0 3.6.57 1 1 0 0 1 1 1V20a1 1 0 0 1-1 1A17 17 0 0 1 3 4a1 1 0 0 1 1-1h3.5a1 1 0 0 1 1 1c0 1.250.2 2.450.57 3.6a1 1 0 0 1-.25 1z"/></svg>
        555-204-7316
      </li>
      <li>
        <svg viewBox="0 0 24 24"><rect x="2" y="5" width="20" height="14" rx="2" fill="var(--green-dark)"/><path d="M3 6l9 7 9-7" fill="none" stroke="var(--white)" stroke-width="1.8"/></svg>
        tobias@korble.example
      </li>
      <li>
        <svg viewBox="0 0 24 24"><g fill="none" stroke="var(--green-dark)" stroke-width="2"><circle cx="12" cy="12" r="10"/><ellipse cx="12" cy="12" rx="4" ry="10"/><path d="M2 12h20M4 7h16M4 17h16"/></g></svg>
        www.weekendwicketleague.example
      </li>
    </ul>
    <p class="company company-first">Korble</p>
    <p class="company company-second">Development</p>
  </section>

  <section class="card back">
    <div class="brand-mark"><span class="dot"></span>WWL</div>
    <h2 class="title">Weekend Wicket League</h2>
    <p class="tagline">The World's Premier Fantasy Cricket Game</p>
  </section>

</main>
</body>
</html>
```